Business cards - Yoga Instructor
Quiet Fern Yoga
Creative Brief
Use same font as used in my logo
Use fonts that you feel work well with the logo and style of card
Bright & Fun-filled
Miriam Tovbrask
Certified Yoga Instructor
Brindle Cove, Oregon
mtovbrask@brightpost.example
www.Quietfern.example
The front should include the "Quiett Fern Yoga" logo that we have uploaded. Also - we would like to include "Offering Veyolin based yoga" on the card as well. perhaps just below the title "Certified Yoga Instructor"
we would like to have the "Ohm" symbol on the back of the card and the words "Strength - Stability - Freedom". here is a link for a sample of the symbol. http://www.breathwheelsite.example/ok.htm We are thinking the Ohm symbol can fill the entire back (even going off the edges) and the text on top.

```html
<!DOCTYPE html>
<html lang="en">
<head>
<meta charset="utf-8">
<title>Quiet Fern Yoga – Business Cards</title>
<link rel="stylesheet" href="https://fonts.googleapis.com/css2?family=Open+Sans:ital,wght@0,400;0,600;0,700;1,400&display=swap">
<style>
  :root {
    --backdrop: #e9e7e4;
    --card: #ffffff;
    --ink: #1d1d1f;
    --ink-soft: #4a4a50;
    --magenta: #b8338c;
    --pink: #e3a6c6;
    --lavender: #a7abdb;
    --lavender-pale: #d6d8f0;
  }
  * { box-sizing: border-box; margin: 0; padding: 0; }
  html, body { width: 1200px; height: 838px; overflow: hidden; }
  body {
    background: var(--backdrop);
    font-family: "Open Sans", Arial, sans-serif;
    position: relative;
  }
  .card {
    position: absolute;
    background: var(--card);
    box-shadow: 0 4px 14px rgba(0,0,0,.18);
    overflow: hidden;
  }
  .card--front { left: 197px; top: 24px; width: 552px; height: 360px; }
  .card--back  { left: 473px; top: 444px; width: 559px; height: 362px; }
  .card__swooshes { position: absolute; inset: 0; width: 100%; height: 100%; }

  .identity {
    position: absolute; right: 18px; top: 16px; text-align: right;
  }
  .identity__name { font-size: 21px; font-weight: 700; color: var(--ink); line-height: 1.2; }
  .identity__title { font-size: 13px; color: var(--ink); margin-top: 2px; }
  .identity__offer { font-size: 12px; font-style: italic; color: var(--magenta); margin-top: 2px; }

  .brand {
    position: absolute; left: 20px; top: 238px;
    display: flex; align-items: center; gap: 10px;
  }
  .brand__name { font-size: 30px; font-weight: 400; color: var(--magenta); }
  .brand__dot { width: 14px; height: 14px; border-radius: 50%; background: var(--magenta); }

  .contact {
    position: absolute; right: 18px; bottom: 22px; text-align: right;
    font-size: 12.5px; line-height: 1.45; color: var(--ink-soft); font-style: normal;
  }

  .motto {
    position: absolute; left: 28px; top: 36px;
    font-size: 19px; color: var(--magenta);
  }
  .om-area {
    position: absolute; left: 340px; top: 96px;
    width: 172px; height: 182px; border-radius: 36px;
    background: radial-gradient(circle at 40% 40%, #d0489f, #a3297c);
  }
</style>
</head>
<body>
  <section class="card card--front">
    <svg class="card__swooshes" viewBox="0 0 680 389" preserveAspectRatio="none" aria-hidden="true">
      <path d="M0,28 C200,18 400,70 680,178" fill="none" stroke="var(--lavender)" stroke-width="7" opacity=".8"/>
      <path d="M40,6 C250,20 450,80 680,160" fill="none" stroke="var(--pink)" stroke-width="3" opacity=".9"/>
      <path d="M0,48 C220,40 420,100 680,196" fill="none" stroke="var(--lavender-pale)" stroke-width="4"/>
      <path d="M0,350 C220,348 430,290 680,215" fill="none" stroke="var(--lavender)" stroke-width="8" opacity=".85"/>
      <path d="M0,370 C240,360 440,310 680,238" fill="none" stroke="var(--lavender-pale)" stroke-width="5"/>
      <path d="M30,335 C240,328 440,272 680,200" fill="none" stroke="var(--pink)" stroke-width="2.5" opacity=".8"/>
    </svg>
    <div class="identity">
      <p class="identity__name">Miriam Tovbrask</p>
      <p class="identity__title">Certified Yoga Instructor</p>
      <p class="identity__offer">"Offering Veyolin based yoga"</p>
    </div>
    <div class="brand">
      <span class="brand__name">Quiet Fern Yoga</span>
      <span class="brand__dot"></span>
    </div>
    <address class="contact">
      Brindle Cove, Oregon<br>
      (512)-555-0148<br>
      mtovbrask@brightpost.example<br>
      www.Quietfern.example
    </address>
  </section>

  <section class="card card--back">
    <svg class="card__swooshes" viewBox="0 0 680 389" preserveAspectRatio="none" aria-hidden="true">
      <path d="M0,230 C220,250 430,150 680,70" fill="none" stroke="var(--lavender)" stroke-width="8" opacity=".85"/>
      <path d="M0,250 C240,268 450,175 680,95" fill="none" stroke="var(--lavender-pale)" stroke-width="5"/>
      <path d="M0,205 C210,222 420,130 680,52" fill="none" stroke="var(--pink)" stroke-width="3" opacity=".9"/>
      <path d="M0,275 C250,290 460,205 680,125" fill="none" stroke="var(--lavender-pale)" stroke-width="3"/>
    </svg>
    <p class="motto">Strength - Stability - Freedom</p>
    <div class="om-area" role="img" aria-label="Large magenta Om symbol"></div>
  </section>
</body>
</html>
```